Bright Horizon Painting and Remodeling needs a business card

Business card should have company logo. I will upload two different logos and let me see which one is a better design for the business card.

Name of company: Bright Horizon Painting and Remodeling
Address: 4126 NW 71st st Suite 214
Miami, FL 33166

local phone: (305) 555-0142
toll free (855) 555-0197
fax (866) 555-0163

email: corinne@paintingbrighthorizon.example

not sure if i should include social media links or names on the business card.

company does interior and exterior painting, pressure washing, wall paper removal, drywall and stucco repair, staining,

We give free estimates.

I want a two sided business card.

Not sure if all this information is necessary for the business card. Designer can pick out whatever information they deem is important for a consumer to see on the business card.

Anticipating on the business card to be printed on nice quality.

I will upload an image of one of the logos on a type of business card surface. That idea can be used as well. Be creative. Business card should be professional but very nice and eye catching.

remove drywall and stucco repair and replace with tile installation

Industry/Entity Type

Business

Contact Information for Business Card

Miami, FL 33166

toll free (855) 555-0197
fax (866) 555-0163

company does interior and exterior painting, pressure washing, wall paper removal, drywall and stucco repair, staining, tile removal, *specializing in vinyl floor removal

free estimates.

Requirements
Must have
• Profesional font

```html
<!DOCTYPE html>
<html lang="en">
<head>
<meta charset="utf-8">
<title>Bright Horizon Painting and Remodeling – Business Card</title>
<link rel="stylesheet" href="https://fonts.googleapis.com/css2?family=Open+Sans:wght@400;700&display=swap">
<style>
  :root {
    --backdrop: #e9e9eb;
    --card: #fbfbfb;
    --ink: #3b3b3f;
    --ink-soft: #5a5a60;
    --rule: #d6d6da;
    --paint-red: #e8453c;
    --paint-blue: #4f83c6;
    --paint-sky: #86b6e2;
    --paint-purple: #9d70c6;
    --paint-orange: #f08c3e;
    --paint-green: #8fcf5a;
  }
  * { box-sizing: border-box; margin: 0; padding: 0; }
  html, body {
    width: 1200px; height: 1000px; overflow: hidden;
    background: var(--backdrop);
    font-family: "Open Sans", Arial, sans-serif;
    color: var(--ink);
  }
  .card {
    position: absolute;
    width: 700px; height: 400px;
    left: 250px;
    background: var(--card);
    border-radius: 26px;
    overflow: hidden;
    box-shadow: 0 10px 28px rgba(0,0,0,.18);
  }
  .card--front { top: 60px; }
  .card--back { top: 540px; }
  .paint-splash { position: absolute; left: 0; top: 0; width: 700px; }
  .brand {
    position: absolute;
    display: flex; align-items: center; gap: 12px;
  }
  .brand__mark {
    width: 30px; height: 30px; border-radius: 50%;
    background: var(--paint-purple);
  }
  .brand__name {
    font-weight: 700; font-size: 15px; line-height: 1.25;
    color: var(--ink); width: 190px;
  }
  .card--front .brand { left: 40px; bottom: 40px; }
  .card--back .brand { left: 40px; bottom: 60px; }
  .divider {
    position: absolute; left: 300px; top: 240px;
    width: 1px; height: 120px; background: var(--rule);
  }
  .contact {
    position: absolute; left: 330px; top: 225px;
    font-size: 15px; line-height: 1.45; color: var(--ink-soft);
  }
  .contact__address { margin-bottom: 8px; }
  .contact__row { display: flex; align-items: center; gap: 10px; }
  .contact__icon { width: 13px; height: 13px; fill: var(--ink); flex: none; }
  .contact__row--plain { padding-left: 23px; }
</style>
</head>
<body>

<section class="card card--front" aria-label="Business card front">
  <svg class="paint-splash" height="290" viewBox="0 0 700 290" role="img" aria-label="Colourful paint splatter in red, blue, purple and orange">
    <defs>
      <linearGradient id="front-paint" x1="0" y1="0" x2="1" y2="0.4">
        <stop offset="0" stop-color="var(--paint-sky)"/>
        <stop offset="0.35" stop-color="var(--paint-red)"/>
        <stop offset="0.65" stop-color="var(--paint-blue)"/>
        <stop offset="1" stop-color="var(--paint-purple)"/>
      </linearGradient>
    </defs>
    <path d="M0 0 H700 V210 C620 240 560 200 490 250 C420 290 360 230 290 260 C220 285 150 230 90 250 C50 262 20 240 0 250 Z" fill="url(#front-paint)" opacity="0.85"/>
  </svg>
  <div class="brand">
    <span class="brand__mark"></span>
    <span class="brand__name">Bright Horizon Painting and Remodeling</span>
  </div>
</section>

<section class="card card--back" aria-label="Business card back">
  <svg class="paint-splash" height="200" viewBox="0 0 700 200" role="img" aria-label="Paint splatter band in purple, blue, orange and red">
    <defs>
      <linearGradient id="back-paint" x1="0" y1="1" x2="1" y2="0">
        <stop offset="0" stop-color="var(--paint-purple)"/>
        <stop offset="0.3" stop-color="var(--paint-orange)"/>
        <stop offset="0.6" stop-color="var(--paint-sky)"/>
        <stop offset="0.85" stop-color="var(--paint-red)"/>
        <stop offset="1" stop-color="var(--paint-green)"/>
      </linearGradient>
    </defs>
    <path d="M0 200 C60 170 120 150 200 120 C280 90 360 100 430 60 C500 25 600 20 700 0 V130 C650 110 600 100 560 70 C470 100 380 150 290 150 C200 160 110 200 40 200 Z" fill="url(#back-paint)" opacity="0.75"/>
  </svg>
  <div class="brand">
    <span class="brand__mark"></span>
    <span class="brand__name">Bright Horizon Painting and Remodeling</span>
  </div>
  <div class="divider"></div>
  <address class="contact" style="font-style:normal">
    <p class="contact__address">4126 NW 71st st Suite 214<br>Miami, FL 33166</p>
    <p class="contact__row">
      <svg class="contact__icon" viewBox="0 0 16 16"><path d="M3.5 1 L6 1 L7 4.5 L5.3 5.8 C6.2 7.8 8.2 9.8 10.2 10.7 L11.5 9 L15 10 L15 12.5 C15 13.9 13.9 15 12.5 15 C6.7 15 1 9.3 1 3.5 C1 2.1 2.1 1 3.5 1 Z"/></svg>
      (305) 555-0142
    </p>
    <p class="contact__row contact__row--plain">(855) 555-0197</p>
    <p class="contact__row">
      <svg class="contact__icon" viewBox="0 0 16 16"><path d="M4 1 H10 L12 3 V6 H4 Z M1 7 H15 V13 H12 V11 H4 V13 H1 Z M5 12 H11 V15 H5 Z"/></svg>
      (866) 555-0163
    </p>
    <p class="contact__row">
      <svg class="contact__icon" viewBox="0 0 16 16"><path d="M1 3 H15 V13 H1 Z M2 4.2 V5 L8 9 L14 5 V4.2 Z" fill-rule="evenodd"/></svg>
      corinne@paintingbrighthorizon.example
    </p>
  </address>
</section>

</body>
</html>
```